Tellbrook Mechanical Heating and Air Conditioning web page

This is a repair, installation and maintenance residential company. I don't do commercial. I need a web design that shows a company with 24/7 fast service that is easy for customers to contact me from. I am a Varnell /Oskiro HVAC dealer and their logos can be on there also. I also sell IAQ products like Zuvo- Crest and I offer duct cleanings as well.

Industry/Entity Type

Hvac

Coding

Coded - Design and coding required

Number of Pages Required

2 page

```html
<!DOCTYPE html>
<html lang="en">
<head>
<meta charset="utf-8">
<title>Tellbrook Mechanical – Heating &amp; Air Conditioning</title>
<link rel="stylesheet" href="https://fonts.googleapis.com/css2?family=Montserrat:wght@400;500;600;700&family=Play:wght@400;700&family=Oswald:wght@600&display=swap">
<style>
:root{
  --blue:#0aa6e6;
  --red:#ec1c24;
  --ink:#1a1a1a;
  --text:#333;
  --muted:#555;
  --card:#f3f3f3;
  --line:#e2e2e2;
  --black:#0b0b0b;
  --white:#fff;
}
*{margin:0;padding:0;box-sizing:border-box}
html,body{width:1200px;height:3891px;overflow:hidden;background:var(--white)}
body{position:relative;font-family:"Montserrat",sans-serif;color:var(--text)}
.abs{position:absolute}
.head-font{font-family:"Play",sans-serif}
.btn{position:absolute;display:flex;align-items:center;justify-content:center;border-radius:20px;color:var(--white);font-size:12px;font-weight:500;background:var(--blue)}
.btn.red{background:var(--red)}
.ph{position:absolute}

/* top bar */
.topbar{left:0;top:0;width:1200px;height:30px;background:var(--blue);color:var(--white);font-size:12px}
.topbar .contact{position:absolute;top:8px;display:flex;align-items:center;gap:7px}
.social-top{position:absolute;top:0;height:30px;display:flex}
.social-top span{width:36px;height:30px;display:flex;align-items:center;justify-content:center}
.social-top span i{width:12px;height:12px;border-radius:2px;background:var(--white);display:block}

/* header */
.logo{position:absolute;display:flex;align-items:center;gap:8px;font-weight:700;font-size:25px;line-height:1.05;color:var(--ink)}
.logo b{display:block;width:14px;height:14px;background:var(--red)}
.nav{position:absolute;top:85px;font-size:13px;color:var(--ink)}
.nav.active{color:var(--red)}

/* hero */
.hero-bg{left:0;top:152px;width:1200px;height:600px;background:linear-gradient(90deg,#eeeeee 0%,#f4f4f4 40%,#d9dadb 100%)}
.hero-tag{left:112px;top:316px;font-family:"Oswald",sans-serif;font-size:25px;color:var(--red);letter-spacing:.5px}
.hero-title{left:112px;top:356px;font-size:40px;line-height:50px;color:var(--ink);width:360px}
.hero-text{left:112px;top:463px;width:340px;font-size:12px;line-height:15px;color:var(--ink)}
.arrow{position:absolute;width:40px;height:40px;border-radius:50%;display:flex;align-items:center;justify-content:center;font-size:16px}

/* sections */
.sec-title{position:absolute;left:0;width:1200px;text-align:center;font-size:30px;color:var(--ink)}
.rule{position:absolute;left:585px;width:30px;height:2px;background:var(--red)}
.center-text{position:absolute;left:262px;width:676px;text-align:center;font-size:12.5px;line-height:15px;color:var(--text)}

.tabs{left:415px;top:1091px;width:374px;height:39px;border-radius:20px;overflow:hidden;display:flex;font-family:"Play",sans-serif;font-weight:700;font-size:17px;color:var(--white)}
.tabs div{display:flex;align-items:center;justify-content:center}
.tabs .heat{width:180px;background:var(--red);border-radius:0 20px 20px 0;position:relative;z-index:1}
.tabs .air{flex:1;background:var(--blue);margin-left:-20px;padding-left:20px}

.svc{position:absolute;top:1159px;width:303px;height:361px;background:var(--card)}
.svc.lift{box-shadow:0 3px 12px rgba(0,0,0,.15);background:#f6f6f6}
.svc .img{position:absolute;left:9px;top:9px;width:285px;height:178px}
.svc .badge{position:absolute;left:136px;top:163px;width:32px;height:32px;border-radius:50%;background:var(--white);display:flex;align-items:center;justify-content:center}
.svc h3{position:absolute;top:214px;width:100%;text-align:center;font-size:12.5px;font-weight:500;color:var(--ink)}
.svc .u{position:absolute;top:234px;left:136px;width:30px;height:2px;background:var(--ink)}
.svc p{position:absolute;top:255px;left:26px;width:251px;text-align:center;font-size:11px;line-height:14.5px;color:var(--ink)}
.svc .go{position:absolute;left:141px;top:320px;width:21px;height:21px;border:1.5px solid var(--ink);border-radius:50%;display:flex;align-items:center;justify-content:center}

/* band */
.band{left:0;top:1653px;width:1200px;height:452px;background:linear-gradient(90deg,#5b5a5c 0%,#6a6a6d 45%,#7d7f86 100%)}
.band-shade{left:560px;top:1653px;width:640px;height:452px;background:linear-gradient(90deg,rgba(70,70,74,0) 0%,rgba(70,72,80,.55) 35%,rgba(70,72,80,.55) 100%)}
.band h2{position:absolute;left:641px;top:1768px;font-size:25px;font-weight:400;color:var(--white)}
.band-text{left:641px;top:1845px;width:440px;font-size:12px;line-height:14.5px;color:var(--white)}
.check{position:absolute;left:644px;display:flex;align-items:center;gap:10px;font-size:12px;color:var(--white)}

/* blogs */
.blog{position:absolute;top:2218px;width:307px;height:373px;background:var(--card)}
.blog.lift{box-shadow:0 3px 12px rgba(0,0,0,.15);background:#f6f6f6}
.blog .img{position:absolute;left:0;top:8px;width:307px;height:193px}
.blog .date{position:absolute;left:14px;top:217px;font-size:11.5px;display:flex;align-items:center;gap:7px;color:var(--ink)}
.blog h4{position:absolute;left:14px;top:241px;font-size:11px;font-weight:600;color:var(--ink)}
.blog p{position:absolute;left:14px;top:281px;width:285px;font-size:11px;line-height:14.5px;color:var(--ink)}
.blog a{position:absolute;left:14px;top:341px;font-size:12px;color:var(--ink);text-decoration:underline}

/* testimonials */
.tcard{position:absolute;top:2785px;width:304px;height:305px;background:var(--card);border:1px solid #ececec;text-align:center}
.tcard .av{position:absolute;left:101px;top:29px;width:102px;height:102px;border-radius:50%}
.tcard .name{position:absolute;top:147px;width:100%;font-size:15px;color:var(--ink)}
.tcard .role{position:absolute;top:168px;width:100%;font-size:14px;color:var(--ink)}
.tcard p{position:absolute;top:195px;left:30px;width:244px;font-size:12px;line-height:15px;color:var(--muted)}
.tcard.lift p{color:var(--ink);font-weight:500}
.stars{position:absolute;top:256px;width:100%;color:#f6a623;font-size:11px;letter-spacing:4px}

/* quote */
.quote-bg{left:0;top:3173px;width:1200px;height:470px;background:linear-gradient(90deg,#e9e7e6 0%,#ecebea 55%,#f1f0ef 100%)}
.quote-title{left:642px;top:3238px;font-size:30px;color:var(--ink)}
.quote-text{left:642px;top:3284px;width:446px;font-size:12px;line-height:13px;color:var(--ink)}
.field{position:absolute;height:35px;background:var(--white);border:1px solid var(--line);font-size:12px;color:var(--ink);padding-left:11px;display:flex;align-items:center}

/* footer */
.footer{left:0;top:3600px;width:1200px;height:236px;background:var(--black);color:var(--white)}
.f-head{position:absolute;font-size:11.5px;color:var(--white)}
.f-link{position:absolute;left:405px;font-size:12.5px;color:var(--white);display:flex;gap:9px}
.f-item{position:absolute;left:612px;font-size:12px;color:var(--white);display:flex;align-items:center;gap:14px}
.bottom{left:0;top:3836px;width:1200px;height:55px;background:var(--white)}
.copy{left:111px;top:3855px;font-size:12px;color:var(--ink)}
.dot-s{position:absolute;top:3847px;width:27px;height:27px;border-radius:50%;background:var(--black)}
.dot-s.b{background:var(--blue)}
</style>
</head>
<body>

<!-- Top bar -->
<div class="abs topbar">
  <div class="contact" style="left:112px">
    <svg width="12" height="12" viewBox="0 0 24 24"><path fill="#fff" d="M6.6 10.8a15 15 0 0 0 6.6 6.6l2.2-2.2c.3-.3.7-.4 1-.2 1.1.4 2.3.6 3.6.6.6 0 1 .4 1 1V20c0 .6-.4 1-1 1A17 17 0 0 1 3 4c0-.6.4-1 1-1h3.5c.6 0 1 .4 1 1 0 1.3.2 2.5.6 3.6.1.3 0 .7-.2 1z"/></svg>
    555 014 2208
  </div>
  <div class="contact" style="left:520px">
    <svg width="15" height="11" viewBox="0 0 16 11"><rect x=".5" y=".5" width="15" height="10" fill="none" stroke="#fff"/><path d="M.5.5 8 6l7.5-5.5" fill="none" stroke="#fff"/></svg>
    hello@tellbrook.example
  </div>
  <svg class="abs" style="left:900px;top:0" width="300" height="30"><polygon points="30,0 300,0 300,30 0,30" fill="#ec1c24"/></svg>
  <div class="social-top" style="left:949px">
    <span><i></i></span><span><i></i></span><span><i></i></span><span><i></i></span>
  </div>
</div>

<!-- Header -->
<div class="logo" style="left:112px;top:70px"><b></b><span>Tellbrook<br>Mechanical</span></div>
<div class="nav active" style="left:491px">Home</div>
<div class="abs" style="left:491px;top:150px;width:36px;height:2px;background:var(--red)"></div>
<div class="nav" style="left:565px">About us</div>
<div class="nav" style="left:660px">Our Services</div>
<div class="nav" style="left:781px">News</div>
<div class="nav" style="left:854px">Contact us</div>
<div class="btn" style="left:958px;top:71px;width:145px;height:39px">Get A Quote</div>

<!-- Hero -->
<div class="abs hero-bg"></div>
<div class="ph" role="img" aria-label="Technician installing a wall-mounted air conditioner" style="left:470px;top:152px;width:730px;height:540px;background:linear-gradient(90deg,rgba(240,240,240,0) 0%,#e6e6e6 20%,#d2d4d6 55%,#c9c0b6 80%,#d8d8da 100%)"></div>
<div class="abs hero-tag">24/7 FAST SERVICE</div>
<div class="abs hero-title head-font">Cooling your Future with Technology</div>
<div class="abs hero-text">Lorem Ipsum is a simply dummy text of the printing typesetting an industry has been the industry.</div>
<div class="btn" style="left:112px;top:515px;width:157px;height:38px">Read More</div>
<div class="arrow" style="left:16px;top:385px;background:#e3e3e3;color:#333">&lt;</div>
<div class="arrow" style="left:1139px;top:385px;background:var(--red);color:#fff">&gt;</div>
<svg class="abs" style="left:0;top:640px" width="1200" height="210" viewBox="0 0 1200 210">
  <path d="M0 100 C300 20 700 10 1200 60 L1200 68 C700 30 300 60 100 120 C60 135 20 160 0 185 Z" fill="#ec1c24"/>
  <path d="M0 185 C20 160 60 135 100 120 C300 60 700 30 1200 68 L1200 210 L0 210 Z" fill="#fff"/>
</svg>
<svg class="abs" style="left:0;top:660px" width="1200" height="60" viewBox="0 0 1200 60"><path d="M300 40 C600 -5 900 0 1200 42 L1200 46 C900 8 600 5 300 40Z" fill="#ec1c24"/></svg>

<!-- About -->
<div class="sec-title head-font" style="top:752px">About us</div>
<div class="rule" style="top:796px"></div>
<div class="center-text" style="top:818px">Lorem Ipsum is a simply dummy text of the printing and typesetting an industry has been the industry's standard an dummy text ever since the 1500s,</div>
<div class="center-text" style="top:864px">when an unknown printer took a galley of type and scrambled it to make a type specimen book. It has survived not only five centuries, but also the leap into electronic typesetting, remaining essentially unchanged it was popularised in the 1960s with the release of Typeset sheets containing Lorem Ipsum passages, and more recently with desktop layout tools including versions of Lorem Ipsum.</div>
<div class="btn" style="left:523px;top:965px;width:157px;height:38px">Read More</div>

<!-- Services -->
<div class="sec-title head-font" style="top:1040px">Services</div>
<div class="abs tabs"><div class="heat">Heating</div><div class="air">Air Conditioning</div></div>

<div class="arrow" style="left:34px;top:1319px;background:#ececec;color:#333">&lt;</div>
<div class="arrow" style="left:1124px;top:1319px;background:#ececec;color:#333">&gt;</div>

<div class="svc" style="left:112px">
  <div class="img" role="img" aria-label="Couple relaxing on a sofa under an air conditioner" style="background:linear-gradient(180deg,#e8e6e2 0%,#d9d4cc 55%,#d7c23a 85%,#c9b530 100%)"></div>
  <div class="badge"><svg width="18" height="16" viewBox="0 0 18 16"><path d="M9 1 1 8h2.5v7h4v-4h3v4h4V8H17z" fill="#ec1c24"/></svg></div>
  <h3>RESIDENTIAL</h3><div class="u"></div>
  <p>Lorem Ipsum is a simply dummy text of the printing and typesetting industry it has been dummy text ever since the 1500s,</p>
  <div class="go"><svg width="8" height="8" viewBox="0 0 8 8"><path d="M2.5 1 5.5 4 2.5 7" fill="none" stroke="#1a1a1a" stroke-width="1.5"/></svg></div>
</div>
<div class="svc lift" style="left:449px">
  <div class="img" role="img" aria-label="Technician checking pressure gauges on a unit" style="background:linear-gradient(135deg,#3a4a6a 0%,#8a6a4a 45%,#b09070 70%,#6a7a8a 100%)"></div>
  <div class="badge"><svg width="16" height="16" viewBox="0 0 16 16"><circle cx="6" cy="5" r="3.5" fill="#ec1c24"/><path d="M7 7 13 14" stroke="#ec1c24" stroke-width="3"/></svg></div>
  <h3>REPAIR</h3><div class="u"></div>
  <p>Lorem Ipsum is a simply dummy text of the printing and typesetting industry it has been dummy text ever since the 1500s,</p>
  <div class="go"><svg width="8" height="8" viewBox="0 0 8 8"><path d="M2.5 1 5.5 4 2.5 7" fill="none" stroke="#1a1a1a" stroke-width="1.5"/></svg></div>
</div>
<div class="svc" style="left:787px">
  <div class="img" role="img" aria-label="Technician installing an indoor air conditioning unit" style="background:linear-gradient(90deg,#f1f1f1 0%,#e4e5e6 45%,#7a8aa8 75%,#e6e6e6 100%)"></div>
  <div class="badge"><svg width="18" height="18" viewBox="0 0 18 18"><circle cx="9" cy="9" r="5" fill="none" stroke="#ec1c24" stroke-width="3"/><g stroke="#ec1c24" stroke-width="2.5"><path d="M9 1v3M9 14v3M1 9h3M14 9h3M3.3 3.3l2.1 2.1M12.6 12.6l2.1 2.1M3.3 14.7l2.1-2.1M12.6 5.4l2.1-2.1"/></g></svg></div>
  <h3>INSTALLATION</h3><div class="u"></div>
  <p>Lorem Ipsum is a simply dummy text of the printing and typesetting industry it has been dummy text ever since the 1500s,</p>
  <div class="go"><svg width="8" height="8" viewBox="0 0 8 8"><path d="M2.5 1 5.5 4 2.5 7" fill="none" stroke="#1a1a1a" stroke-width="1.5"/></svg></div>
</div>
<div class="btn" style="left:523px;top:1567px;width:157px;height:38px">View More</div>

<!-- Heating & Air band -->
<div class="abs band" role="img" aria-label="Hands holding red and blue manifold pressure gauges"></div>
<div class="abs band-shade"></div>
<div class="band abs" style="background:none">
  <h2 class="head-font">Heating &amp; Air Conditioning</h2>
</div>
<div class="abs band-text">Lorem Ipsum is a simply dummy text of the printing and typesetting an industry has been the industry's standard an dummy text ever since the 1500s,</div>
<div class="check" style="top:1910px"><svg width="18" height="18" viewBox="0 0 18 18"><circle cx="9" cy="9" r="8" fill="none" stroke="#fff" stroke-width="1.3"/><path d="M5 9.5 8 12.5 14 5" fill="none" stroke="#fff" stroke-width="1.6"/></svg>Cool Air</div>
<div class="check" style="top:1937px"><svg width="18" height="18" viewBox="0 0 18 18"><circle cx="9" cy="9" r="8" fill="none" stroke="#fff" stroke-width="1.3"/><path d="M5 9.5 8 12.5 14 5" fill="none" stroke="#fff" stroke-width="1.6"/></svg>Speedy service</div>
<div class="btn" style="left:641px;top:1987px;width:157px;height:38px">Read More</div>
<div class="btn red" style="left:810px;top:1987px;width:157px;height:38px">Contact us</div>

<!-- Latest Blogs -->
<div class="sec-title head-font" style="top:2159px">Latest Blogs</div>
<div class="blog" style="left:113px">
  <div class="img" role="img" aria-label="Bright living room with a wall air conditioner and remote" style="background:linear-gradient(180deg,#b9bbbd 0%,#cfd0d0 50%,#e9e9e7 100%)"></div>
  <div class="date"><svg width="12" height="12" viewBox="0 0 12 12"><circle cx="6" cy="6.5" r="4.6" fill="none" stroke="#ec1c24" stroke-width="1.3"/><path d="M6 4v3l1.8 1" fill="none" stroke="#ec1c24" stroke-width="1.2"/></svg>April 14, 2020</div>
  <h4>What is Lorem Ipsum?</h4>
  <p>Lorem Ipsum is simply dummy text the printing and typesetting industry Lorem Ipsum has been dummy text ever since the 1500s,</p>
  <a>Continue..</a>
</div>
<div class="blog lift" style="left:447px">
  <div class="img" role="img" aria-label="Woman on a sofa pointing a remote at an air conditioner" style="background:linear-gradient(180deg,#8a8c8c 0%,#9c9d9b 45%,#d8d4cc 80%,#ece8e0 100%)"></div>
  <div class="date"><svg width="12" height="12" viewBox="0 0 12 12"><circle cx="6" cy="6.5" r="4.6" fill="none" stroke="#ec1c24" stroke-width="1.3"/><path d="M6 4v3l1.8 1" fill="none" stroke="#ec1c24" stroke-width="1.2"/></svg>April 14, 2020</div>
  <h4>What is Lorem Ipsum?</h4>
  <p>Lorem Ipsum is simply dummy text the printing and typesetting industry Lorem Ipsum has been dummy text ever since the 1500s,</p>
  <a>Continue..</a>
</div>
<div class="blog" style="left:780px">
  <div class="img" role="img" aria-label="Technician cleaning an air conditioner filter" style="background:linear-gradient(90deg,#d6d8da 0%,#c8ccd0 40%,#8c98a8 70%,#d0d2d4 100%)"></div>
  <div class="date"><svg width="12" height="12" viewBox="0 0 12 12"><circle cx="6" cy="6.5" r="4.6" fill="none" stroke="#ec1c24" stroke-width="1.3"/><path d="M6 4v3l1.8 1" fill="none" stroke="#ec1c24" stroke-width="1.2"/></svg>April 14, 2020</div>
  <h4>What is Lorem Ipsum?</h4>
  <p>Lorem Ipsum is simply dummy text the printing and typesetting industry Lorem Ipsum has been dummy text ever since the 1500s,</p>
  <a>Continue..</a>
</div>
<div class="btn" style="left:523px;top:2616px;width:157px;height:38px">View More</div>

<!-- Testimonials -->
<div class="sec-title head-font" style="top:2696px">Testimonials</div>
<div class="abs" style="left:0;top:2740px;width:1200px;text-align:center;font-size:11.5px;color:var(--ink)">What Clients say about us</div>
<div class="tcard" style="left:115px">
  <div class="av" role="img" aria-label="Client portrait" style="background:radial-gradient(circle,#b8a898 0%,#5a4e46 100%)"></div>
  <div class="name">Mirela Dovanski</div><div class="role">Director</div>
  <p>Lorem Ipsum is simply dummy of the printing and typesetting Lorem Ipsum industry.</p>
  <div class="stars">★★★★★</div>
</div>
<div class="tcard lift" style="left:446px">
  <div class="av" role="img" aria-label="Client portrait" style="background:radial-gradient(circle,#d0b8a0 0%,#6e5e50 100%)"></div>
  <div class="name">Corinne Valt</div><div class="role">Director</div>
  <p>Lorem Ipsum is simply dummy of the printing and typesetting Lorem Ipsum industry.</p>
  <div class="stars">★★★★★</div>
</div>
<div class="tcard" style="left:783px">
  <div class="av" role="img" aria-label="Client portrait" style="background:radial-gradient(circle,#b0a8a4 0%,#3e4250 100%)"></div>
  <div class="name">Tobias Renner</div><div class="role">Director</div>
  <p>Lorem Ipsum is simply dummy of the printing and typesetting Lorem Ipsum industry.</p>
  <div class="stars">★★★★★</div>
</div>
<div class="abs" style="left:583px;top:3116px;width:6px;height:6px;border-radius:50%;background:var(--red)"></div>
<div class="abs" style="left:597px;top:3116px;width:6px;height:6px;border-radius:50%;background:#888"></div>
<div class="abs" style="left:611px;top:3116px;width:6px;height:6px;border-radius:50%;background:#888"></div>

<!-- Request a Quote -->
<div class="abs quote-bg"></div>
<div class="ph" role="img" aria-label="Indoor air conditioning unit mounted on the wall" style="left:397px;top:3173px;width:454px;height:32px;background:linear-gradient(180deg,#2a2a2a 0%,#3a3a3a 40%,#f4f4f4 45%,#e8e8e8 100%);border-radius:0 0 6px 6px"></div>
<div class="ph" role="img" aria-label="Smiling woman holding an air conditioner remote" style="left:140px;top:3220px;width:440px;height:390px;background:radial-gradient(ellipse at 50% 55%,#b7b3b0 0%,#d2cfcc 45%,rgba(233,231,230,0) 75%)"></div>
<div class="abs quote-title head-font">Request a Quote</div>
<div class="abs quote-text">Lorem Ipsum simply dummy text the printing and ypesetting and dummy Ipsum is simply dummy text of the printing.</div>
<div class="field" style="left:642px;top:3333px;width:216px">First Name</div>
<div class="field" style="left:869px;top:3333px;width:217px">Last Name</div>
<div class="field" style="left:642px;top:3380px;width:216px">Phone</div>
<div class="field" style="left:869px;top:3380px;width:217px">Email</div>
<div class="field" style="left:642px;top:3424px;width:444px;justify-content:space-between;padding-right:10px">Intrested in <svg width="8" height="6" viewBox="0 0 8 6"><path d="M1 1.5 4 4.5 7 1.5" fill="none" stroke="#333"/></svg></div>
<div class="btn" style="left:639px;top:3472px;width:157px;height:38px">Send Now</div>

<!-- Footer -->
<svg class="abs" style="left:0;top:3555px" width="1200" height="90" viewBox="0 0 1200 90">
  <path d="M0 60 C300 5 800 0 1200 40 L1200 90 L0 90Z" fill="#ec1c24"/>
  <path d="M0 90 C300 40 800 42 1200 55 L1200 90Z" fill="#0b0b0b"/>
</svg>
<div class="abs footer">
  <div class="logo" style="left:113px;top:94px;color:#fff"><b></b><span>Tellbrook<br>Mechanical</span></div>
  <div class="f-head" style="left:405px;top:32px">Quick Links</div>
  <div class="f-link" style="top:61px"><span>›</span>Home</div>
  <div class="f-link" style="top:84px"><span>›</span>About us</div>
  <div class="f-link" style="top:106px"><span>›</span>Our Services</div>
  <div class="f-link" style="top:129px"><span>›</span>Gallery</div>
  <div class="f-link" style="top:151px"><span>›</span>Blog</div>
  <div class="f-link" style="top:174px"><span>›</span>Contact us</div>

  <div class="f-head" style="left:612px;top:32px">Contact information</div>
  <div class="f-item" style="top:61px"><svg width="12" height="12" viewBox="0 0 24 24"><path fill="#fff" d="M6.6 10.8a15 15 0 0 0 6.6 6.6l2.2-2.2c.3-.3.7-.4 1-.2 1.1.4 2.3.6 3.6.6.6 0 1 .4 1 1V20c0 .6-.4 1-1 1A17 17 0 0 1 3 4c0-.6.4-1 1-1h3.5c.6 0 1 .4 1 1 0 1.3.2 2.5.6 3.6.1.3 0 .7-.2 1z"/></svg>(00) 555 014 2208</div>
  <div class="f-item" style="top:85px"><svg width="13" height="9" viewBox="0 0 16 11"><rect x=".5" y=".5" width="15" height="10" fill="#fff"/><path d="M.5.5 8 6l7.5-5.5" fill="none" stroke="#0b0b0b"/></svg>hello@tellbrook.example</div>
  <div class="f-item" style="top:110px"><svg width="12" height="13" viewBox="0 0 12 16"><path d="M6 0a6 6 0 0 0-6 6c0 4.5 6 10 6 10s6-5.5 6-10a6 6 0 0 0-6-6zm0 8.5A2.5 2.5 0 1 1 6 3.5a2.5 2.5 0 0 1 0 5z" fill="#fff"/></svg>4780 Larchmere Road</div>
  <div class="f-item" style="top:136px;left:645px">Dunvale, KY, Kentucky</div>
  <div class="f-item" style="top:162px;left:645px">ZipCode : 40999</div>

  <div class="f-head" style="left:876px;top:32px">Join Our Mailing List</div>
  <div class="abs" style="left:876px;top:55px;width:210px;font-size:11.5px;line-height:12px">Lorem Ipsum simply dummy text typesetting and dummy.</div>
  <div class="field" style="left:878px;top:98px;width:208px;height:33px">Your Email</div>
  <div class="btn" style="left:878px;top:140px;width:208px;height:33px">Submit</div>
</div>
<div class="abs bottom"></div>
<div class="abs copy">Copyright © 2020 Tellbrook Mechanical. All Right Reserved</div>
<div class="dot-s b" style="left:953px"></div>
<div class="dot-s" style="left:988px"></div>
<div class="dot-s" style="left:1023px"></div>
<div class="dot-s" style="left:1058px"></div>

</body>
</html>
```